Scholarly Pathways - educational consulting

I am beginning an educational consultation business - focusing on Tribal (Native American Indian) Communities, but will work with anyone. I have work experience in K-12 and Higher Education. Special Education - transition from school to work. Advising and facilitating with academic skills in higher education. I have a BS - Special Education, Masters - Educational Administration and working on a PhD in Higher Education. Also completing PMB approved certification as an Academic Life Coach

Target Market(s)

K12 college bound students and parents, Kinfolk Crossings college bound students and families, special education college bound students and parents

Industry/Entity Type

Business

Contact Information for Business Card

Marnie Odell Fenwick. PO Box 417, Cushing, OK 74023. (918) 555-0293. marnie@scholarlypathways.example

Requirements
Must have
• Scholarly Pathways is the name of the business - Kinfolk Crossings is a focus area
Nice to have
• Tourquoise would be nice. I do not have a logo yet

```html
<!DOCTYPE html>
<html lang="en">
<head>
<meta charset="utf-8">
<title>Scholarly Pathways – Business Cards</title>
<link href="https://fonts.googleapis.com/css2?family=Josefin+Sans:wght@300;400&display=swap" rel="stylesheet">
<style>
  :root {
    --bg: #2a2a2c;
    --card: #050505;
    --pink: #ee1a8c;
    --white: #ffffff;
    --ink: #111111;
  }
  * { margin: 0; padding: 0; box-sizing: border-box; }
  html, body { width: 1200px; height: 801px; overflow: hidden; }
  body {
    background: var(--bg);
    font-family: "Josefin Sans", sans-serif;
    font-weight: 300;
    color: var(--white);
    display: flex;
    align-items: center;
    justify-content: center;
    gap: 44px;
  }
  .card {
    position: relative;
    width: 520px;
    height: 297px;
    background: var(--card);
    overflow: hidden;
    box-shadow: 0 10px 30px rgba(0,0,0,.45);
  }

  /* Front */
  .card--front {
    display: flex;
    flex-direction: column;
    align-items: center;
    justify-content: center;
  }
  .brand-name {
    color: var(--pink);
    font-weight: 400;
    font-size: 30px;
    letter-spacing: 1px;
    white-space: nowrap;
  }
  .front-holder {
    margin-top: 22px;
    font-size: 17px;
    letter-spacing: 1.5px;
    text-transform: uppercase;
    white-space: nowrap;
  }
  .tagline {
    color: var(--pink);
    font-size: 6.5px;
    letter-spacing: 3.2px;
    text-transform: uppercase;
    margin-top: 6px;
    white-space: nowrap;
  }

  /* Back */
  .brand-block {
    position: absolute;
    left: 22px;
    top: 150px;
    width: 200px;
    text-align: center;
  }
  .brand-block .brand-name { font-size: 20px; }
  .brand-block .tagline { font-size: 5px; letter-spacing: 2.3px; margin-top: 10px; }

  .details {
    position: absolute;
    left: 240px;
    top: 76px;
    padding-left: 12px;
    border-left: 1.5px solid var(--pink);
    white-space: nowrap;
  }
  .holder-name {
    font-size: 18px;
    letter-spacing: 1px;
    text-transform: uppercase;
    margin-bottom: 6px;
  }
  .credentials {
    color: var(--pink);
    font-size: 5.5px;
    letter-spacing: .6px;
    line-height: 1.6;
    text-transform: uppercase;
    margin-bottom: 10px;
  }
  .contact-line {
    display: flex;
    align-items: center;
    gap: 7px;
    font-size: 12px;
    letter-spacing: .8px;
    text-transform: uppercase;
    margin-bottom: 4px;
  }
  .contact-line svg { width: 11px; height: 13px; flex: none; }

  .service-band {
    position: absolute;
    left: 0; right: 0; bottom: 0;
    height: 46px;
    background: var(--white);
    padding: 10px 14px 0;
    text-align: right;
    white-space: nowrap;
  }
  .service-band__marker {
    position: absolute;
    top: -9px;
    right: 98px;
    width: 14px;
    height: 10px;
  }
  .services {
    color: var(--ink);
    font-size: 6.4px;
    font-weight: 400;
    letter-spacing: .7px;
    text-transform: uppercase;
  }
  .certification {
    color: var(--pink);
    font-size: 10px;
    letter-spacing: .8px;
    text-transform: uppercase;
    margin-top: 5px;
  }
</style>
</head>
<body>

  <section class="card card--front">
    <div class="brand-name">Scholarly Pathways</div>
    <div class="front-holder">Marnie Odell Fenwick</div>
    <div class="tagline">Educational Consultation Business</div>
  </section>

  <section class="card card--back">
    <div class="brand-block">
      <div class="brand-name">Scholarly Pathways</div>
      <div class="tagline">Educational Consultation Business</div>
    </div>

    <div class="details">
      <div class="holder-name">Marnie Odell Fenwick</div>
      <div class="credentials">
        Masters – Educational Administration / PhD in Higher Ed<br>
        BS – Special Education
      </div>
      <div class="contact-line">
        <svg viewBox="0 0 11 13" aria-hidden="true">
          <rect x="1.5" y="0.75" width="8" height="11.5" rx="1.2" fill="none" stroke="#ee1a8c" stroke-width="1.2"/>
          <line x1="4" y1="10.3" x2="7" y2="10.3" stroke="#ee1a8c" stroke-width="1"/>
        </svg>
        <span>555.555.0293</span>
      </div>
      <div class="contact-line">
        <svg viewBox="0 0 11 13" aria-hidden="true">
          <path d="M0.5 6.5 L5.5 1.5 L10.5 6.5 L9 6.5 L9 12 L2 12 L2 6.5 Z" fill="#ee1a8c"/>
        </svg>
        <span>P.O. Box 417 Larkfield, ST 00417</span>
      </div>
    </div>

    <div class="service-band">
      <svg class="service-band__marker" viewBox="0 0 14 10" aria-hidden="true">
        <polygon points="7,0 14,10 0,10" fill="#ee1a8c"/>
      </svg>
      <div class="services">K-12 and Higher Education &#9632; Advising and Facilitating with Academic Skills in Higher Education</div>
      <div class="certification">PMB Approved Certification as an Academic Life Coach</div>
    </div>
  </section>

</body>
</html>
```